TK Joinery

Cabinet maker. Kitchens. Wardrobes. Vanitys. Entertainment units

Target Market(s)

Modern contemporary.geometry. colours black, gray, charcoal and orange. Matt card gloss letters

Industry/Entity Type

Entertainment

Contact Information for Business Card

Mattias Velder 0418 295 437
mattias.velder@fernmail.test
ABN 471 9052 8316

Font styles to use
Decorative

Colors
000000

Requirements
Should not have
• Pictures

```html
<!DOCTYPE html>
<html lang="en">
<head>
<meta charset="UTF-8">
<title>TK Joinery — Business Card</title>
<link rel="stylesheet" href="https://fonts.googleapis.com/css2?family=Kalam:wght@400;700&display=swap">
<style>
  :root {
    --backdrop: #7a7a7a;
    --card: #000000;
    --orange: #f05323;
    --orange-dim: #6a2410;
    --light-grey: #d6d6d6;
    --mid-grey: #8c8c8c;
    --white: #ffffff;
  }
  html, body {
    margin: 0;
    padding: 0;
    width: 1200px;
    height: 1200px;
    overflow: hidden;
    background: var(--backdrop);
  }
  .canvas {
    position: relative;
    width: 1200px;
    height: 1200px;
    font-family: "Kalam", cursive;
  }
  .card {
    position: absolute;
    left: 283px;
    width: 683px;
    height: 421px;
    background: var(--card);
  }
  .card--front { top: 167px; }
  .card--back { top: 611px; }

  .brand-name {
    position: absolute;
    margin: 0;
    font-weight: 700;
    line-height: 1;
    white-space: nowrap;
  }
  .card--front .brand-name {
    left: 62px;
    top: 152px;
    font-size: 50px;
    color: var(--light-grey);
  }
  .divider {
    position: absolute;
    left: 303px;
    top: 98px;
    width: 1px;
    height: 195px;
    background: var(--orange-dim);
  }
  .contact {
    position: absolute;
    left: 335px;
    top: 108px;
  }
  .contact__name {
    margin: 0 0 26px;
    font-size: 27px;
    font-weight: 700;
    color: var(--orange);
    line-height: 1;
  }
  .contact__line {
    display: flex;
    align-items: center;
    gap: 10px;
    margin: 0;
    height: 28px;
    font-size: 18px;
    color: var(--white);
  }
  .contact__line svg { width: 13px; height: 13px; flex: none; }
  .contact__abn {
    margin: 16px 0 0;
    font-size: 18px;
    color: var(--white);
  }
  .contact__abn .label { color: var(--orange); margin-right: 8px; }
  .services {
    position: absolute;
    left: 66px;
    top: 343px;
    display: flex;
    gap: 34px;
    margin: 0;
    padding: 0;
    list-style: none;
    font-size: 19px;
    color: var(--white);
  }
  .services li::before {
    content: "";
    display: inline-block;
    width: 7px;
    height: 7px;
    margin-right: 6px;
    border-radius: 50%;
    background: var(--orange);
    vertical-align: middle;
  }
  .card--back .brand-name {
    left: 0;
    right: 0;
    top: 150px;
    text-align: center;
    font-size: 84px;
    color: var(--mid-grey);
  }
</style>
</head>
<body>
<main class="canvas">
  <section class="card card--front">
    <p class="brand-name">TK Joinery</p>
    <span class="divider"></span>
    <div class="contact">
      <p class="contact__name">Mattias Velder</p>
      <p class="contact__line">
        <svg viewBox="0 0 24 24" aria-hidden="true"><path fill="var(--orange)" d="M6.6 10.8a15.5 15.5 0 0 0 6.6 6.6l2.2-2.2c.3-.3.7-.4 1-.2 1.1.4 2.3.6 3.6.6.6 0 1 .4 1 1V20c0 .6-.4 1-1 1A17 17 0 0 1 3 4c0-.6.4-1 1-1h3.5c.6 0 1 .4 1 1 0 1.3.2 2.5.6 3.6.1.3 0 .7-.2 1z"/></svg>
        0418 295 437
      </p>
      <p class="contact__line">
        <svg viewBox="0 0 24 24" aria-hidden="true"><path fill="var(--orange)" d="M2 5h20v14H2z"/><path fill="none" stroke="#000" stroke-width="2" d="M2 5l10 8 10-8"/></svg>
        mattias.velder@fernmail.test
      </p>
      <p class="contact__abn"><span class="label">ABN Number:</span>471 9052 8316</p>
    </div>
    <ul class="services">
      <li>Kitchens</li>
      <li>Wardrobes</li>
      <li>Vanitys</li>
      <li>Entertainment Units</li>
    </ul>
  </section>

  <section class="card card--back">
    <p class="brand-name">TK Joinery</p>
  </section>
</main>
</body>
</html>
```